Varelick Bright Foundation - Brochure

We need a brochure for this foundation to get donations. It needs to have the information provided plus a spot for a credit card number, expiration date and signature. We need people to open their hearts and give to this organization that is just getting started. The information is there. We just need it to look more classy and professional.

Target Market(s)

businesses, fraternal organizations, residents

Industry/Entity Type

Non Profit

Colors
ec1f27
3277b5
ffffff

Requirements
Must have
• all the information included. logo is set.

```html
<!DOCTYPE html>
<html lang="en">
<head>
<meta charset="utf-8">
<title>Varelick Bright Foundation – Brochure</title>
<link href="https://fonts.googleapis.com/css2?family=Alfa+Slab+One&family=Lato:ital,wght@0,400;0,700;1,400&display=swap" rel="stylesheet">
<style>
:root{
  --navy:#1f2c6b;
  --red:#c61f31;
  --ink:#222;
  --black:#1b1b1b;
  --white:#fff;
  --stage:#d3d3d3;
  --grey-text:#444;
  --grass:#6f9a45;
  --rule:#9a9a9a;
}
*{margin:0;padding:0;box-sizing:border-box}
html,body{width:933px;height:1200px;overflow:hidden}
body{background:var(--stage);font-family:"Lato",sans-serif;color:var(--ink);position:relative}
.spread{position:absolute;left:30px;width:873px;height:560px;display:flex;box-shadow:0 6px 18px rgba(0,0,0,.25)}
.spread--outer{top:20px}
.spread--inner{top:620px}
.panel{position:relative;width:436.5px;height:100%;background:var(--white);overflow:hidden}
.display{font-family:"Alfa Slab One",serif;font-weight:400;text-transform:uppercase;letter-spacing:.5px}
.photo{position:absolute;background:linear-gradient(160deg,#8fae6a 0%,var(--grass) 55%,#4f7a32 100%)}
.brand{font-family:"Lato",sans-serif;font-weight:700;color:var(--navy);text-transform:uppercase;letter-spacing:2px;display:flex;align-items:center;gap:7px}
.brand::before{content:"";width:12px;height:12px;border-radius:50%;background:var(--navy);flex:none}

/* back panel */
.back__head{position:absolute;top:0;left:0;right:0;height:108px;background:var(--black);padding:34px 26px 0;color:var(--white);font-size:18px;line-height:1.2;white-space:nowrap}
.back__body{position:absolute;top:108px;left:0;right:0;bottom:0;background:linear-gradient(180deg,#c9cdc4 0%,#b9c0b0 100%)}
.back__text{position:absolute;top:16px;left:26px;right:24px;font-size:12.5px;line-height:1.3;color:var(--grey-text)}
.back__text p+p{margin-top:10px}
.back__photo1{left:26px;top:212px;width:120px;height:92px}
.back__photo2{left:154px;top:206px;width:120px;height:74px}
.back__brand{position:absolute;left:288px;top:236px;width:132px;font-size:9px;letter-spacing:1px;line-height:1.25;align-items:center}
.back__brand::before{width:10px;height:10px}
.back__band{position:absolute;left:0;right:0;bottom:0;height:200px;background:var(--navy);clip-path:polygon(0 44%,100% 0,100% 100%,0 100%)}
.contact{position:absolute;left:26px;bottom:14px;color:var(--white)}
.contact__title{font-size:19px;margin-bottom:4px}
.contact__row{display:flex;align-items:center;gap:12px;font-size:14px;margin-top:5px}
.contact__row svg{width:14px;height:14px;flex:none}
.social{position:absolute;right:30px;bottom:110px;display:flex;gap:8px}
.social span{width:26px;height:26px;background:var(--white)}

/* front panel */
.front__brand{position:absolute;top:34px;left:0;right:0;justify-content:center;font-size:17px}
.front__photo{left:0;right:0;top:84px;height:218px;background:linear-gradient(180deg,#9fb98a 0%,#7da35a 30%,var(--grass) 60%,#5d8c3a 100%)}
.mission{position:absolute;left:0;right:0;top:302px;height:92px;background:var(--red);color:var(--white);text-align:center;padding:12px 22px 0;font-size:11.5px;line-height:1.3}
.mission h3{font-weight:400;font-size:13px;margin-bottom:3px}
.services{position:absolute;top:408px;left:0;right:0;text-align:center}
.services h3{font-weight:400;font-size:16px;letter-spacing:.5px;color:#333}
.services__list{display:flex;justify-content:space-around;margin-top:12px;padding:0 14px}
.services__item{display:flex;flex-direction:column;align-items:center;gap:8px;font-size:11.5px;color:#444}
.services__item svg{width:20px;height:20px;fill:var(--navy)}
.more{position:absolute;left:0;right:0;text-align:center;font-size:11.5px;color:#444;line-height:1.5}
.more__url{display:inline-flex;align-items:center;gap:6px;font-size:13px}
.more__url svg{width:12px;height:12px}
.front__more{bottom:20px}

/* inner left */
.help{position:absolute;top:0;left:0;right:0;height:180px;background:var(--red);color:var(--white);padding:20px 28px 0;font-style:italic;font-size:13.5px;line-height:1.22}
.help h3{font-weight:400;font-size:11.5px;margin-bottom:6px}
.help ol{list-style:none}
.help li{padding-left:16px;text-indent:-16px}
.help b{font-style:normal}
.uses{position:absolute;top:196px;left:28px;right:24px;font-size:13px;line-height:1.22}
.uses h3,.benefits h3{font-style:italic;font-weight:400;color:var(--navy);font-size:12.5px;margin-bottom:8px}
.uses ol{list-style:none}
.uses li{padding-left:16px;text-indent:-16px}
.inner__photos{position:absolute;top:310px;left:28px;right:24px;display:flex;gap:8px}
.inner__photos .photo{position:static;flex:1;height:100px}
.benefits{position:absolute;top:440px;left:28px;right:24px;font-size:13.5px;line-height:1.2}

/* inner right */
.ask{position:absolute;top:30px;left:26px;right:22px;font-size:19px;line-height:1.05;color:var(--navy)}
.ask em{font-style:normal;color:var(--red)}
.facts{position:absolute;top:110px;left:30px;right:22px;font-size:12.2px;line-height:1.2;color:#333}
.facts li{margin-left:12px;margin-bottom:1px}
.donate{position:absolute;top:346px;left:30px;right:26px;border:1.5px solid var(--navy);padding:8px 12px 10px}
.donate__title{font-size:12px;color:var(--red);margin-bottom:4px}
.donate__row{display:flex;gap:14px;margin-top:8px}
.donate__field{flex:1;display:flex;align-items:flex-end;gap:6px;font-size:11px;color:#333;white-space:nowrap}
.donate__field--exp{flex:0 0 120px}
.donate__line{flex:1;border-bottom:1px solid var(--rule);height:14px}
.inner__brand{position:absolute;left:0;right:0;top:470px;justify-content:center;font-size:18px}
.inner__more{bottom:14px;font-style:italic}
</style>
</head>
<body>

<section class="spread spread--outer">
  <article class="panel back">
    <header class="back__head display">The need in the Cedar Valley<br>has never been greater</header>
    <div class="back__body">
      <div class="back__text">
        <p>When a person becomes an amputee, they are faced with staggering emotional and financial lifestyle changes. Fortunately, high tech prosthetic devices that restore a person’s basic skills and independence are available. Unfortunately, many amputees lack the financial resources to obtain adequate prosthetic care.</p>
        <p>That’s where the Varelick Bright Foundation steps in. Our goal is to provide a financial bridge between those amputees needing assistance and the quality prosthetic care needed to restore their lives.</p>
      </div>
      <div class="photo back__photo1" role="img" aria-label="Amputee golfer mid-swing on a green fairway"></div>
      <div class="photo back__photo2" role="img" aria-label="Amputee golfer chipping from a sand bunker"></div>
      <div class="brand back__brand">Varelick Bright Foundation</div>
    </div>
    <div class="back__band"></div>
    <div class="social" aria-hidden="true"><span></span><span></span><span></span></div>
    <div class="contact">
      <h2 class="contact__title display">Contact us</h2>
      <div class="contact__row"><svg viewBox="0 0 16 16" fill="none" stroke="#fff" stroke-width="1.6"><rect x="4" y="1" width="8" height="14" rx="1.5"/><line x1="7" y1="12.5" x2="9" y2="12.5"/></svg>1-555-014-2947</div>
      <div class="contact__row"><svg viewBox="0 0 16 16" fill="none" stroke="#fff" stroke-width="1.6"><rect x="1.5" y="3.5" width="13" height="9"/><polyline points="1.5,3.5 8,9 14.5,3.5"/></svg>dana@varelickbright.org</div>
      <div class="contact__row"><svg viewBox="0 0 16 16" fill="none" stroke="#fff" stroke-width="1.4"><circle cx="8" cy="8" r="6.5"/><ellipse cx="8" cy="8" rx="3" ry="6.5"/><line x1="1.5" y1="8" x2="14.5" y2="8"/></svg>varelickbright.org</div>
    </div>
  </article>

  <article class="panel front">
    <div class="brand front__brand">Varelick Bright Foundation</div>
    <div class="photo front__photo" role="img" aria-label="Amputee golfer with a prosthetic leg standing on a course beside a pond"></div>
    <div class="mission">
      <h3>Mission Statement:</h3>
      The Varelick Bright Foundation is a non-profit charitable organization established to assist people who have experienced the loss of a limb and are seeking assistance to realize their full potential, and live their lives to the fullest after amputation.
    </div>
    <div class="services">
      <h3>SERVICES</h3>
      <div class="services__list">
        <div class="services__item"><svg viewBox="0 0 24 24"><polygon points="12,1 15,9 23,9 16.5,14 19,22 12,17 5,22 7.5,14 1,9 9,9"/></svg>Financial Assistance</div>
        <div class="services__item"><svg viewBox="0 0 24 24"><polygon points="12,1 15,9 23,9 16.5,14 19,22 12,17 5,22 7.5,14 1,9 9,9"/></svg>Peer support</div>
        <div class="services__item"><svg viewBox="0 0 24 24"><polygon points="12,1 15,9 23,9 16.5,14 19,22 12,17 5,22 7.5,14 1,9 9,9"/></svg>Awareness and Advocacy</div>
      </div>
    </div>
    <div class="more front__more">For more information, please visit our web site<br>
      <span class="more__url"><svg viewBox="0 0 16 16" fill="none" stroke="#c61f31" stroke-width="1.6"><circle cx="8" cy="8" r="6.5"/><ellipse cx="8" cy="8" rx="3" ry="6.5"/><line x1="1.5" y1="8" x2="14.5" y2="8"/></svg>www.varelickbright.org</span></div>
  </article>
</section>

<section class="spread spread--inner">
  <article class="panel">
    <div class="help">
      <h3>How you can help:</h3>
      <ol>
        <li>1) Tell all your friends, neighbors and colleagues about our mission</li>
        <li>2) Visit our web site at <b>www.varelickbright.org</b> and make a donation</li>
        <li>3) Like and share our story online:<br><b>www.varelickbright.org/share</b></li>
      </ol>
    </div>
    <div class="uses">
      <h3>What your donations will be used for:</h3>
      <ol>
        <li>1) Aid in the purchase of prosthetic devices for those unable to pay</li>
        <li>2) Sending kids to Stride Camp</li>
        <li>3) Help qualified amputees access high tech devices to improve their daily lives</li>
      </ol>
    </div>
    <div class="inner__photos">
      <div class="photo" role="img" aria-label="Group of golfers posing with a cheque on the course"></div>
      <div class="photo" role="img" aria-label="Golfer swinging on a tree-lined fairway"></div>
      <div class="photo" role="img" aria-label="Two golfers putting on a green near a pond"></div>
    </div>
    <div class="benefits">
      <h3>Who benefits from our services:</h3>
      We would love to help everyone who applies for a grant, unfortunately that won’t be possible in some cases. If needed, our priorities will be to help children, veterans and then everyone else possible.
    </div>
  </article>

  <article class="panel">
    <h2 class="ask display">We’re not asking<br>for much,<br><em>just an arm and a leg!</em></h2>
    <ul class="facts">
      <li>There are nearly 2 million people living with limb loss in the United States</li>
      <li>Among those living with limb loss, the main causes are vascular disease (54%) – including diabetes and peripheral arterial disease – trauma (45%) and cancer (less than 2%)</li>
      <li>Approximately 185,000 amputations occur in the United States each year</li>
      <li>In 2009, hospital costs associated with amputation totaled more than $8.3 billion</li>
      <li>Nearly half of the individuals who have an amputation due to vascular disease will die within 5 years. This is higher than the five-year mortality rates for breast cancer, colon cancer, and prostate cancer</li>
      <li>The majority of traumatic injury amputees are between the ages of 15-40</li>
      <li>80% of traumatic injury amputees are men</li>
    </ul>
    <form class="donate" aria-label="Donation form">
      <h3 class="donate__title display">Make a donation</h3>
      <div class="donate__row">
        <div class="donate__field">Amount $<span class="donate__line"></span></div>
        <div class="donate__field">Credit card number<span class="donate__line"></span></div>
      </div>
      <div class="donate__row">
        <div class="donate__field donate__field--exp">Exp. date<span class="donate__line"></span></div>
        <div class="donate__field">Signature<span class="donate__line"></span></div>
      </div>
    </form>
    <div class="brand inner__brand">Varelick Bright Foundation</div>
    <div class="more inner__more">For more information, please visit our web site<br>
      <span class="more__url"><svg viewBox="0 0 16 16" fill="none" stroke="#c61f31" stroke-width="1.6"><circle cx="8" cy="8" r="6.5"/><ellipse cx="8" cy="8" rx="3" ry="6.5"/><line x1="1.5" y1="8" x2="14.5" y2="8"/></svg>www.varelickbright.org</span></div>
  </article>
</section>

</body>
</html>
```